Four in One (Flexible infographic for Content Management Industry)

See attachment.
A graphic depicting 4 products, where each can stand on its own and each can be combined with others, but where, if all are taken together, the best result is achieved (the "super product").
Intended use is web. See attached file as an example.
The most basic idea is as the attached diagram shows, where 4 rectangles are arranged in a quadrangle, with a middle rectangle in the center representing the combined 4 products. This concept is fine except it is a bit too obvious as it stands. We are looking for either a variation of this or another concept.
The audience is technical + professional + enterprise - NOT consumers. Hence the design should be conservative in nature.
We are aware of tools like as Canva or Pictogram where such graphics are available, but we are looking for something with a bit more imagination and flexibility.
This graphic should be targeted to web sites and be delivered with vector-based (SVG) graphics.

```html
<!DOCTYPE html>
<html lang="en">
<head>
<meta charset="utf-8">
<title>Four in One – Super Product</title>
<link rel="stylesheet" href="https://fonts.googleapis.com/css2?family=Barlow:wght@500;600;800;900&display=swap">
<style>
:root{
  --page:#ffffff;
  --green-a:#00803c;
  --green-b:#00bd45;
  --indigo-a:#14146e;
  --indigo-b:#383398;
  --charcoal-a:#272727;
  --charcoal-b:#414141;
  --teal-a:#0a3f6a;
  --teal-b:#077184;
  --core-a:#2b55cc;
  --core-b:#1c38a6;
  --bar:#2d49c9;
  --ink:#ffffff;
  --rule:rgba(255,255,255,.45);
}
*{margin:0;padding:0;box-sizing:border-box}
html,body{width:1200px;height:928px;overflow:hidden;background:var(--page)}
.infographic{position:relative;width:1200px;height:928px;font-family:"Barlow",sans-serif;color:var(--ink)}
.backdrop{position:absolute;left:0;top:0}
.pillar{position:absolute;width:342px}
.pillar--left{left:263px}
.pillar--right{left:597px;text-align:right;width:342px}
.pillar__title{font-weight:800;font-size:24px;line-height:29px;letter-spacing:.3px;text-transform:uppercase}
.pillar__text{font-weight:600;font-size:13.4px;line-height:17.4px;letter-spacing:.2px}
.features{list-style:none}
.feature{display:flex;align-items:center;gap:13px;height:27px;font-weight:600;font-size:14px;letter-spacing:.3px;position:relative}
.feature:not(:last-child)::after{content:"";position:absolute;bottom:0;height:1px;width:250px;background:linear-gradient(90deg,var(--rule),rgba(255,255,255,0))}
.pillar--right .feature{justify-content:flex-end}
.pillar--right .feature:not(:last-child)::after{right:0;background:linear-gradient(270deg,var(--rule),rgba(255,255,255,0))}
.tick{width:15px;height:15px;flex:none}
.icon{position:absolute;fill:none;stroke:var(--ink);stroke-width:2.2;stroke-linecap:round;stroke-linejoin:round}
.core-label{position:absolute;left:468px;top:413px;width:260px;text-align:center;font-weight:900;text-transform:uppercase;line-height:48px;letter-spacing:-1px}
.core-label span{display:block}
.core-label .core-label__top{font-size:52px}
.core-label .core-label__bottom{font-size:50px}
</style>
</head>
<body>
<main class="infographic">
  <svg class="backdrop" width="1200" height="928" viewBox="0 0 1200 928">
    <defs>
      <linearGradient id="barV" x1="0" y1="0" x2="0" y2="1">
        <stop offset="0" stop-color="var(--bar)" stop-opacity="0"/>
        <stop offset=".35" stop-color="var(--bar)"/>
        <stop offset=".65" stop-color="var(--bar)"/>
        <stop offset="1" stop-color="var(--bar)" stop-opacity="0"/>
      </linearGradient>
      <linearGradient id="barH" x1="0" y1="0" x2="1" y2="0">
        <stop offset="0" stop-color="var(--bar)" stop-opacity="0"/>
        <stop offset=".3" stop-color="var(--bar)"/>
        <stop offset=".7" stop-color="var(--bar)"/>
        <stop offset="1" stop-color="var(--bar)" stop-opacity="0"/>
      </linearGradient>
      <linearGradient id="fillGreen" x1="0" y1="0" x2="1" y2=".6"><stop offset="0" stop-color="var(--green-a)"/><stop offset=".55" stop-color="var(--green-a)"/><stop offset=".9" stop-color="var(--green-b)"/><stop offset="1" stop-color="var(--green-a)"/></linearGradient>
      <linearGradient id="fillIndigo" x1="0" y1="0" x2="1" y2="1"><stop offset="0" stop-color="var(--indigo-b)"/><stop offset=".35" stop-color="var(--indigo-a)"/><stop offset="1" stop-color="var(--indigo-b)"/></linearGradient>
      <linearGradient id="fillCharcoal" x1="0" y1="0" x2="1" y2="1"><stop offset="0" stop-color="var(--charcoal-a)"/><stop offset=".6" stop-color="var(--charcoal-b)"/><stop offset="1" stop-color="var(--charcoal-a)"/></linearGradient>
      <linearGradient id="fillTeal" x1="0" y1="0" x2="1" y2="1"><stop offset="0" stop-color="var(--teal-b)"/><stop offset=".4" stop-color="var(--teal-a)"/><stop offset="1" stop-color="var(--teal-b)"/></linearGradient>
      <radialGradient id="fillCore" cx=".5" cy=".45" r=".6"><stop offset="0" stop-color="var(--core-a)"/><stop offset="1" stop-color="var(--core-b)"/></radialGradient>
    </defs>
    <rect class="connector" x="588" y="150" width="21" height="630" fill="url(#barV)"/>
    <rect class="connector" x="287" y="451" width="627" height="21" fill="url(#barH)"/>
    <rect class="card card--document" x="237" y="101" width="342" height="341" rx="55" fill="url(#fillGreen)"/>
    <rect class="card card--security" x="618" y="101" width="342" height="341" rx="55" fill="url(#fillIndigo)"/>
    <rect class="card card--erp" x="237" y="482" width="342" height="341" rx="55" fill="url(#fillCharcoal)"/>
    <rect class="card card--digital" x="618" y="482" width="342" height="341" rx="55" fill="url(#fillTeal)"/>
    <circle cx="598" cy="461" r="133" fill="var(--page)"/>
    <circle cx="598" cy="461" r="124" fill="url(#fillCore)" role="img" aria-label="Blue circuit-board texture behind the combined product"/>
    <symbol id="tick" viewBox="0 0 20 20"><path d="M18 8.5A8 8 0 1 1 13.5 3" fill="none" stroke="#fff" stroke-width="1.8" stroke-linecap="round"/><path d="M6.5 10l3 3 8-8" fill="none" stroke="#fff" stroke-width="1.8" stroke-linecap="round" stroke-linejoin="round"/></symbol>
  </svg>

  <svg class="icon" style="left:440px;top:138px" width="50" height="50" viewBox="0 0 50 50">
    <path d="M24 2H10a8 8 0 0 0-8 8v14a6 6 0 0 0 6 6 6 6 0 0 1 6 6v4a8 8 0 0 0 8 8h12a6 6 0 0 0 6-6v-8"/>
    <circle cx="37" cy="13" r="11"/><path d="M32 13l3.5 3.5 6.5-7"/>
  </svg>
  <svg class="icon" style="left:713px;top:140px" width="64" height="60" viewBox="0 0 64 60">
    <path d="M20 42H14a12 12 0 0 1-2-23.8A16 16 0 0 1 42 12a11 11 0 0 1 8 26"/>
    <path d="M32 30l11 4v8c0 7-5 11-11 14-6-3-11-7-11-14v-8z"/><path d="M27 42l4 4 7-8"/>
  </svg>
  <svg class="icon" style="left:409px;top:530px" width="60" height="60" viewBox="0 0 60 60">
    <path d="M49 7v8h-8"/><path d="M11 53v-8h8"/>
    <path d="M49 15A25 25 0 0 0 6 24"/><path d="M11 45a25 25 0 0 0 43-9"/>
    <path d="M30 17l3 3 4-1 1 4 4 2-1 4 2 3-3 3 1 4-4 1-1 4-4-1-2 3-3-3-4 1-1-4-4-2 1-4-2-3 3-3-1-4 4-1 1-4 4 1z"/>
    <circle cx="30" cy="30" r="5"/>
  </svg>
  <svg class="icon" style="left:772px;top:527px" width="52" height="52" viewBox="0 0 52 52">
    <path d="M30 46H10a8 8 0 0 1-8-8V10a8 8 0 0 1 8-8h28a8 8 0 0 1 8 8v16"/>
    <path d="M2 14h44"/><path d="M10 24h4M18 24h10M10 33h4M18 33h6"/>
    <circle cx="39" cy="39" r="8"/><path d="M45 45l5 5"/>
  </svg>

  <section class="pillar pillar--left" style="top:140px">
    <h2 class="pillar__title">Document<br>Management</h2>
    <p class="pillar__text" style="margin-top:15px;width:240px">Streamline document organization, access, and collaboration with easier file storage and sharing, leading to more effecient workflows.</p>
    <ul class="features" style="margin-top:15px">
      <li class="feature"><svg class="tick"><use href="#tick"/></svg>Centralized Document Control</li>
      <li class="feature" style="font-size:13px"><svg class="tick"><use href="#tick"/></svg>Collaborative Workspace Integration</li>
      <li class="feature"><svg class="tick"><use href="#tick"/></svg>Automated Compliance Tracking</li>
      <li class="feature"><svg class="tick"><use href="#tick"/></svg>Check 4</li>
    </ul>
  </section>

  <section class="pillar pillar--right" style="top:140px">
    <h2 class="pillar__title">Security &amp;<br>Compliance</h2>
    <p class="pillar__text" style="margin-top:15px">Benefit from tailored cloud solutions,<br>secure data storage, and expert disaster<br>recovery planning for reliable and scalable<br>IT operations.</p>
    <ul class="features" style="margin-top:17px">
      <li class="feature">Custom cloud Solutions<svg class="tick"><use href="#tick"/></svg></li>
      <li class="feature">Secure Data Storage<svg class="tick"><use href="#tick"/></svg></li>
      <li class="feature">Expert Disaster Recovery<svg class="tick"><use href="#tick"/></svg></li>
      <li class="feature">Check 4<svg class="tick"><use href="#tick"/></svg></li>
    </ul>
  </section>

  <section class="pillar pillar--left" style="top:510px">
    <h2 class="pillar__title">Enterprise<br>Resource<br>Planning</h2>
    <p class="pillar__text" style="margin-top:15px;width:250px">Simplify management across finance, sales, and operations, enabling better decision-making and improved productivity.</p>
    <ul class="features" style="margin-top:14px">
      <li class="feature"><svg class="tick"><use href="#tick"/></svg>&nbsp;Integrated Business Processes</li>
      <li class="feature"><svg class="tick"><use href="#tick"/></svg>&nbsp;Enhanced Decision-Making</li>
      <li class="feature"><svg class="tick"><use href="#tick"/></svg>&nbsp;Productivity Improvement</li>
      <li class="feature"><svg class="tick"><use href="#tick"/></svg>&nbsp;Check 4</li>
    </ul>
  </section>

  <section class="pillar pillar--right" style="top:560px">
    <h2 class="pillar__title">Digital<br>Transformation</h2>
    <p class="pillar__text" style="margin-top:14px">Turn scanned documents into easily<br>searchable digital archives, boosting<br>effeciency and accessibility.</p>
    <ul class="features" style="margin-top:13px">
      <li class="feature">Instant searchable Archives with OCR<svg class="tick"><use href="#tick"/></svg></li>
      <li class="feature">Automated Document Classification<svg class="tick"><use href="#tick"/></svg></li>
      <li class="feature">DocuHub and Cloud Blob Ready<svg class="tick"><use href="#tick"/></svg></li>
      <li class="feature">Check 4<svg class="tick"><use href="#tick"/></svg></li>
    </ul>
  </section>

  <h1 class="core-label"><span class="core-label__top">Super</span><span class="core-label__bottom">Product</span></h1>
</main>
</body>
</html>
```